corvel antique auction

traditional auction house website. example : tarquelauction.com, dorvickinc.com, marnobrastel.com

Industry/Entity Type

House

Number of Pages Required

5+ page

```html
<!DOCTYPE html>
<html lang="en">
<head>
<meta charset="utf-8">
<title>Corvel Antique Auction</title>
<link href="https://fonts.googleapis.com/css2?family=Source+Sans+3:ital,wght@0,400;0,600;1,400;1,600&family=Montserrat:wght@400;500;600&family=Lora:ital@1&display=swap" rel="stylesheet">
<style>
:root{
  --teal:#1f7f7a;
  --teal-dark:#16645f;
  --orange:#e8832c;
  --rust:#b85d12;
  --ink:#3a3a3a;
  --muted:#6a6a6a;
  --green:#6aa52f;
  --page:#ffffff;
  --bg:#2b2526;
  --line:#d9d9d9;
}
*{margin:0;padding:0;box-sizing:border-box}
html,body{width:791px;height:1200px;overflow:hidden;background:var(--bg);font-family:"Source Sans 3",sans-serif;color:var(--ink)}
.canvas{position:relative;width:791px;height:1200px}
.abs{position:absolute}
.topbar{left:66px;top:0;width:660px;height:4px;background:var(--rust)}
.page{left:66px;top:4px;width:660px;height:1028px;background:var(--page)}
.btn-sm{height:12px;font:600 7px/12px "Source Sans 3",sans-serif;color:#fff;padding:0 4px;border-radius:1px}
.login{left:554px;top:16px;background:var(--orange)}
.register{left:601px;top:16px;background:var(--teal)}
.lang{left:660px;top:15px;font-size:8px;display:flex;align-items:center;gap:4px}
.flag{width:14px;height:9px;background:#3b4f8a;border:1px solid #c23}
.logo{left:78px;top:31px;width:166px;height:50px;border:2px solid var(--orange);border-radius:3px;display:flex;align-items:center;justify-content:center;font:400 12.5px "Montserrat",sans-serif;color:#555;white-space:nowrap;overflow:hidden}
.social{top:56px;width:19px;height:19px;border:1px solid #2a8ab8;border-radius:50%}
.search{left:662px;top:54px;width:48px;height:20px;border:1px solid #9cc86e}
.nav{left:78px;top:107px;width:638px;height:33px;background:var(--teal);border-radius:3px;display:flex;justify-content:center;align-items:center}
.nav a{color:#fff;text-decoration:none;font:600 10px "Source Sans 3",sans-serif;padding:0 8px;border-left:1px solid #4fa39d}
.nav a:first-child{border-left:none}
.nav a.on{color:#111}
.drop{left:262px;top:142px;width:87px}
.drop div{height:12px;font:600 6px/12px "Source Sans 3",sans-serif;color:#fff;padding-left:13px}
.drop .d1{background:#111}.drop .d2{background:var(--teal)}
.slider{left:78px;top:148px;width:638px;height:210px;background:linear-gradient(180deg,#9cc4e0 0%,#d9c7a8 45%,#c9a47a 70%,#5f8a3e 100%)}
.arrow{top:238px;width:27px;height:33px;background:#1a1a1a}
.dots{left:362px;top:338px;width:68px;height:18px;background:#fff;border-radius:3px 3px 0 0;display:flex;justify-content:center;align-items:center;gap:5px}
.dots i{width:7px;height:7px;border-radius:50%;background:#b8b8b8}
.dots i.on{background:var(--teal)}
.welcome{left:80px;top:402px;font:400 21px "Source Sans 3",sans-serif;color:#333}
.welcome em{color:var(--teal);font-style:italic}
.intro{left:80px;top:437px;width:396px;font-size:12px;font-weight:400;line-height:18.4px;color:#444}
.item{left:83px;width:400px;height:146px}
.thumb{position:absolute;left:0;top:0;width:151px;height:90px;border:3px solid #b9b9b9}
.item h3{position:absolute;left:162px;top:2px;width:200px;font:400 15px/19px "Source Sans 3",sans-serif;color:#333}
.meta{position:absolute;left:163px;top:44px;font-size:9px;color:var(--green)}
.desc{position:absolute;left:163px;top:62px;width:245px;font-size:6.4px;font-weight:400;line-height:11px;color:#555}
.links{position:absolute;left:16px;top:99px;font-size:10px;color:#444;display:flex;gap:10px;align-items:center}
.links span+span{border-left:1px solid #ccc;padding-left:10px}
.bid{position:absolute;left:163px;top:102px;width:107px;height:15px;background:var(--teal);border-radius:2px;color:#fff;font:600 7px/15px "Source Sans 3",sans-serif;text-align:center}
.sep{position:absolute;left:0;top:124px;width:400px;height:1px;background:var(--line)}
.seeall{left:81px;top:980px;font:italic 13px "Source Sans 3",sans-serif;color:var(--orange);text-decoration:underline}
.pg{top:982px;height:16px;background:var(--teal);color:#fff;font:600 7.5px/16px "Source Sans 3",sans-serif;text-align:center;border-radius:1px}
.feat{left:519px;top:413px;width:196px;height:177px;border:2px solid #e2e2e2;border-radius:3px}
.ribbon{left:513px;top:426px;width:133px;height:19px;background:var(--teal);color:#fff;font:600 10px/19px "Source Sans 3",sans-serif;padding-left:11px;clip-path:polygon(0 0,100% 0,92% 100%,0 100%)}
.fold{left:513px;top:445px;width:0;height:0;border-top:9px solid var(--teal-dark);border-left:6px solid transparent}
.fnav{left:690px;top:429px;width:19px;height:11px;border:1px solid #555;display:flex}
.fnav i{flex:1;font:700 8px/9px sans-serif;color:#333;text-align:center;font-style:normal}
.fimg{left:533px;top:458px;width:165px;height:70px;border:2px solid #ccc;background:linear-gradient(180deg,#a9c8e2,#76808e 60%,#6a8c4d)}
.ftitle{left:534px;top:536px;font:600 7.5px "Source Sans 3",sans-serif;color:#222}
.ftext{left:534px;top:550px;width:160px;font-size:5.6px;font-weight:400;line-height:8px;color:#666}
.video{left:522px;top:640px;width:190px;height:113px;background:linear-gradient(180deg,#5c6a74,#8a5a3c 55%,#3d4a2c)}
.news{left:518px;top:805px;width:198px;height:123px;background:linear-gradient(180deg,#2a9a92,#146b63);border-radius:3px;color:#fff}
.news h4{position:absolute;left:12px;top:10px;font:600 14px "Source Sans 3",sans-serif}
.news p{position:absolute;left:12px;top:36px;width:170px;font-size:7.5px;line-height:10.5px}
.email{position:absolute;left:13px;top:67px;width:176px;height:24px;background:#fff;border-radius:3px;border:1px solid #0f5a54}
.email span{position:absolute;left:12px;top:7px;font:italic 7.5px "Source Sans 3",sans-serif;color:#777}
.email b{position:absolute;right:0;top:0;width:32px;height:22px;border-left:2px solid var(--teal)}
.foot{font-family:"Montserrat",sans-serif;color:#fff}
.fco{left:94px;top:1062px;font-size:12.5px;font-weight:500}
.faddr{left:96px;top:1081px;font-size:8.6px;line-height:15.6px}
.faddr div{display:flex;align-items:center;gap:5px}
.fh{top:1052px;font-size:18px;font-weight:500}
.quote{left:314px;top:1068px;font:700 46px/1 Georgia,serif;color:var(--teal)}
.qtext{left:347px;top:1080px;width:190px;font:italic 11px/14px "Lora",serif;color:#ddd}
.qby{left:381px;top:1143px;font-size:11.5px;font-weight:500}
.badges{left:582px;top:1086px;width:129px;height:36px;background:#fff;display:flex;justify-content:space-around;align-items:center;padding:0 6px}
.badges i{width:22px;height:24px;background:#2a2a2a;border-radius:2px}
.copy{left:0;top:1184px;width:791px;height:16px;background:var(--rust);color:#f3d9c0;font:7px/16px "Source Sans 3",sans-serif;text-align:center}
</style>
</head>
<body>
<div class="canvas">
  <div class="abs page"></div>
  <div class="abs topbar"></div>

  <div class="abs btn-sm login">Log in</div>
  <div class="abs btn-sm register">Register</div>
  <div class="abs lang"><span class="flag"></span>Eng ▾</div>

  <div class="abs logo">Corvel Antique Auction</div>
  <div class="abs social" style="left:555px"></div>
  <div class="abs social" style="left:579px"></div>
  <div class="abs social" style="left:604px"></div>
  <div class="abs social" style="left:629px;border-color:var(--orange)"></div>
  <div class="abs search">
    <svg width="48" height="20"><circle cx="36" cy="9" r="3.5" fill="none" stroke="#bbb" stroke-width="1.3"/><line x1="38.5" y1="11.5" x2="42" y2="15" stroke="#bbb" stroke-width="1.5"/></svg>
  </div>

  <nav class="abs nav">
    <a>Home</a><a class="on">Auctions</a><a>Auction Services</a><a>Our Company</a><a>Contact Us</a>
  </nav>

  <div class="abs slider" role="img" aria-label="Photo of a cream two-storey house with slate roof and garden"></div>
  <div class="abs drop"><div class="d1">Upcoming Auctions</div><div class="d2">Past Auctions</div></div>
  <div class="abs arrow" style="left:78px"><svg width="27" height="33"><path d="M16 10 L10 16.5 L16 23" fill="none" stroke="#fff" stroke-width="3"/></svg></div>
  <div class="abs arrow" style="left:689px"><svg width="27" height="33"><path d="M11 10 L17 16.5 L11 23" fill="none" stroke="#fff" stroke-width="3"/></svg></div>
  <div class="abs dots"><i></i><i class="on"></i><i></i><i></i></div>

  <h1 class="abs welcome">Welcome to <em>Name of your site</em></h1>
  <p class="abs intro">Lorem ipsum dolor sit amet, consectetur adipisicing elit, sed do eiusmod tempor incididunt ut labore et dolore magna aliqua. Ut enim ad minimdol veniam, quis nostrud exercitation ullamco laboris nisi ut aliquip ex ea commodo consequat. Duis aute irure dolor.</p>

  <article class="abs item" style="top:544px">
    <div class="thumb" role="img" aria-label="Photo of a modern white and grey family house" style="background:linear-gradient(180deg,#6f9bd0,#d8d4cc 55%,#8c8a84)"></div>
    <h3>Lorem ipsum dolor sit amet, consect etur adipisicing...</h3>
    <div class="meta">September 24 &nbsp;•&nbsp; 14 Comments</div>
    <p class="desc">Lorem ipsum dolor sit amet, consectetur adipisicing elit, sed do eiusmod tempor incididunt ut labore et dolore magna aliqua. Ut enim ad minim veniam, quis nostrud exercitation ullamco laboris nisi ut.</p>
    <div class="links"><span>🔍︎ Details</span><span>▣ Gallery</span></div>
    <div class="bid">Click here to bid online</div>
    <div class="sep"></div>
  </article>

  <article class="abs item" style="top:690px">
    <div class="thumb" role="img" aria-label="Photo of a large white colonial house with porch" style="background:linear-gradient(180deg,#3f8ad6,#f1efe9 50%,#4f7a3a)"></div>
    <h3>Lorem ipsum dolor sit amet, consect etur adipisicing...</h3>
    <div class="meta">September 24 &nbsp;•&nbsp; 14 Comments</div>
    <p class="desc">Lorem ipsum dolor sit amet, consectetur adipisicing elit, sed do eiusmod tempor incididunt ut labore et dolore magna aliqua. Ut enim ad minim veniam, quis nostrud exercitation ullamco laboris nisi ut.</p>
    <div class="links"><span>🔍︎ Details</span><span>▣ Gallery</span></div>
    <div class="bid">Click here to bid online</div>
    <div class="sep"></div>
  </article>

  <article class="abs item" style="top:836px">
    <div class="thumb" role="img" aria-label="Photo of a stone house surrounded by flowering garden" style="background:linear-gradient(180deg,#7fb2e0,#8a8276 50%,#4f8a36)"></div>
    <h3>Lorem ipsum dolor sit amet, consect etur adipisicing...</h3>
    <div class="meta">September 24 &nbsp;•&nbsp; 14 Comments</div>
    <p class="desc">Lorem ipsum dolor sit amet, consectetur adipisicing elit, sed do eiusmod tempor incididunt ut labore et dolore magna aliqua. Ut enim ad minim veniam, quis nostrud exercitation ullamco laboris nisi ut.</p>
    <div class="links"><span>🔍︎ Details</span><span>▣ Gallery</span></div>
    <div class="bid">Click here to bid online</div>
    <div class="sep"></div>
  </article>

  <div class="abs seeall">See All</div>
  <div class="abs pg" style="left:130px;width:34px">Prev.</div>
  <div class="abs pg" style="left:170px;width:34px">Next</div>

  <aside>
    <div class="abs feat"></div>
    <div class="abs ribbon">FEATURED AUCTIONS</div>
    <div class="abs fold"></div>
    <div class="abs fnav"><i>‹</i><i style="border-left:1px solid #555">›</i></div>
    <div class="abs fimg" role="img" aria-label="Photo of a grey shingled house with garage"></div>
    <div class="abs ftitle">Lorem Ipsum Dolorum</div>
    <p class="abs ftext">Lorem ipsum dolor sit amet, consectetur adipisicing elit, sed do eiusmod tempor incididunt ut labore et dolore magna aliqua. Ut enim ad minim veniam, quis nostrud.</p>

    <div class="abs video" role="img" aria-label="Video still of a brick house at dusk">
      <svg width="190" height="113"><circle cx="100" cy="56" r="19" fill="none" stroke="#fff" stroke-width="2.5"/><path d="M94 46 L108 56 L94 66 Z" fill="#fff"/><rect x="0" y="108" width="190" height="5" fill="#111"/><rect x="0" y="109" width="10" height="2" fill="#d33"/></svg>
    </div>

    <div class="abs news">
      <h4>Sign up to our Newsletter</h4>
      <p>Lorem ipsum dolor sit amet, consectetur adipisicing elit, sed do eiusmod tempor.</p>
      <div class="email"><span>Enter your Email</span><b><svg width="30" height="22"><path d="M9 11 H21 M16 6 L21 11 L16 16" fill="none" stroke="#6aa52f" stroke-width="2"/></svg></b></div>
    </div>
  </aside>

  <footer class="foot">
    <div class="abs fco">Name of your Company</div>
    <div class="abs faddr">
      <div>218 Verlin Lane, Ashford, AR 70000</div>
      <div><svg width="11" height="8"><rect x="0.5" y="0.5" width="10" height="7" fill="none" stroke="#fff"/><path d="M0.5 0.5 L5.5 4.5 L10.5 0.5" fill="none" stroke="#fff"/></svg>Email: hello@corvelauction.com</div>
      <div><svg width="11" height="11"><circle cx="5.5" cy="5.5" r="5" fill="none" stroke="#fff"/><path d="M3.5 3 Q3.5 7.5 8 8" fill="none" stroke="#fff" stroke-width="1.4"/></svg>Phone: &nbsp;(555) 014-2290</div>
    </div>
    <div class="abs fh" style="left:357px">Testimonials</div>
    <div class="abs quote">“</div>
    <p class="abs qtext">Lorem ipsum is a dummy text only. Dolor sit amet, consectetur adipis cing elit. Nullam felis mauris.</p>
    <div class="abs qby">John Doe, New York</div>
    <div class="abs fh" style="left:590px">Affiliations</div>
    <div class="abs badges"><i></i><i></i><i></i><i></i></div>
    <div class="abs copy">Copyright@Corvel Antique Auction.2015.All Rights Reserved.</div>
  </footer>
</div>
</body>
</html>
```